Design a few pages of a luxury magazine for the Prestige Aubergerie Lyon

We need a luxury design for our magazine. See the inDesign pages of the current version attached (zip).

Please work primarily on the first double page (Inventez le luxe de demain) that contains only one photo with legend, a title and the text both in French and English. It must be made clear that the text is the same in two different languages (it is not clear enough here).

You can also work on the other two double pages selected. Feedback will be provided and the 10 best pages will be submitted to a vote at the end of the project timespan.

The most important is a classy and luxury design, this will be printed on expensive paper.

See the full brochure here: https://www.prestigeaubergerie.com/brochure/#page=4

Target Market(s)

Students and parents

Industry/Entity Type

Education

Colors

Designer to choose colors to be used in the design.

Requirements
Must have
• Luxury magazine layout, see:
• https://www.findwerk.com/search?q=luxury+magazine+layout&client=safari&rls=en&source=lnms&tbm=isch&sa=X&ved=0ahUKEwitoIDmit7fAhUVShUIHXC2Cd4Q_AUIDigB&biw=1010&bih=702
Nice to have
• The color of the cover that should be used for blue and grey is #393d49.
• Our font for serif titles (from the logo) is Adobe TRAJAN.
Should not have
• flashy colors

```html
<!DOCTYPE html>
<html lang="fr">
<head>
<meta charset="utf-8">
<title>Prestige Aubergerie Lyon — Inventez le luxe de demain</title>
<link rel="stylesheet" href="https://fonts.googleapis.com/css2?family=Cinzel:wght@400;500&family=Fira+Sans:ital,wght@0,300;0,400;0,600;1,300;1,600&display=swap">
<style>
  :root {
    --navy: #393d49;
    --gold: #c4a86c;
    --paper: #ffffff;
    --ink: #3b3e48;
    --ink-soft: #555a66;
    --on-navy: #f2f2f4;
  }
  * { margin: 0; padding: 0; box-sizing: border-box; }
  html, body { width: 1200px; height: 764px; overflow: hidden; background: var(--paper); }
  .spread { position: relative; width: 1200px; height: 764px; font-family: "Fira Sans", Arial, sans-serif; color: var(--ink); }

  .french-panel { position: absolute; left: 0; top: 0; width: 301px; height: 764px; background: var(--navy); }
  .header-band { position: absolute; left: 599px; top: 0; width: 601px; height: 77px; background: var(--navy);
    display: flex; align-items: center; justify-content: center; }
  .header-band span { font-family: "Cinzel", "Times New Roman", serif; color: var(--gold); font-size: 15px; letter-spacing: 3.5px; text-transform: uppercase; }

  .title { position: absolute; top: 82px; font-family: "Cinzel", "Times New Roman", serif; font-weight: 400; font-size: 41px; line-height: 53px; }
  .title-fr { left: 40px; width: 232px; text-align: right; color: var(--gold); }
  .title-en { left: 330px; width: 260px; text-align: left; color: var(--navy); }
  .title small { font-size: 41px; }

  .divider { position: absolute; left: 72px; top: 278px; width: 460px; height: 12px; }

  .body { position: absolute; top: 341px; font-size: 10.6px; line-height: 14.4px; font-weight: 300; }
  .body p + p { margin-top: 10px; }
  .body-fr { left: 53px; width: 222px; color: var(--on-navy); }
  .body-en { left: 330px; width: 216px; color: var(--ink-soft); text-align: justify; hyphens: auto; }

  .photo { position: absolute; left: 599px; top: 96px; width: 601px; height: 534px;
    background: radial-gradient(ellipse at 50% 35%, #b59a6e 0%, #6f6450 35%, #3a3b33 70%, #2a2c2a 100%); }
  .photo::after { content: ""; position: absolute; left: 0; right: 0; bottom: 0; height: 150px;
    background: linear-gradient(180deg, rgba(190,180,160,0) 0%, rgba(205,195,175,.75) 100%); }

  .caption { position: absolute; top: 650px; font-size: 7.6px; line-height: 10px; color: var(--ink); }
  .caption b { font-weight: 600; }
  .caption-fr { left: 630px; width: 240px; }
  .caption-en { left: 924px; width: 240px; text-align: right; font-style: italic; }

  .folio { position: absolute; top: 722px; font-size: 8px; font-weight: 600; }
  .folio-left { left: 52px; color: var(--on-navy); }
  .folio-right { left: 1157px; color: var(--ink); }
</style>
</head>
<body>
<main class="spread">
  <section class="french-panel" lang="fr"></section>
  <header class="header-band"><span>À la Prestige Aubergerie</span></header>

  <h1 class="title title-fr" lang="fr">Inventez le LUXE de demain</h1>
  <h2 class="title title-en" lang="en">Invent tomorrow’s luxuries</h2>

  <svg class="divider" viewBox="0 0 460 12" aria-hidden="true">
    <line x1="0" y1="6" x2="460" y2="6" stroke="var(--gold)" stroke-width="1.4"/>
    <circle cx="6" cy="6" r="3" fill="var(--gold)"/>
    <circle cx="454" cy="6" r="3" fill="var(--gold)"/>
  </svg>

  <div class="body body-fr" lang="fr">
    <p>Depuis sa création il y a 30 ans, notre école garde le même objectif : que chaque étudiant acquière les compétences et développe les talents essentiels pour briller dans l’univers du luxe. Première école dédiée à l’hôtellerie de luxe, la Prestige Aubergerie délivre un Bachelor et un Master of Science in International Tourism and Hospitality Management, deux grades universitaires anglais.</p>
    <p>Cette combinaison du luxe à la française et du management anglosaxon donne toutes les clés à nos étudiants pour s’assurer une place privilégiée dans l’univers du luxe en France et à l’international.</p>
    <p>Grâce à l’excellence académique de nos programmes, la dimension internationale de nos formations et l’immersion professionnelle à travers des stages dans les plus prestigieux hôtels du monde, tous nos diplômés sont assurés de faire carrière dans le secteur de leur choix à un poste stratégique. La moitié d’entre eux signent un CDI avant même la fin de leur dernier stage.</p>
  </div>

  <div class="body body-en" lang="en">
    <p>Since its foundation 30 years ago, our school has had only one objective: that each student acquires the skills and develops the essential talents they require to shine within the luxury sector. The Prestige Aubergerie is the first Higher Education establishment dedicated to luxury hotel training: we offer a Bachelor’s and a Master’s degree in International Tourism and Hospitality Management.</p>
    <p>This combination of French-style luxury and Anglo-Saxon management gives our students the key elements they need to ensure a privileged position within the luxury industry both in France and internationally.</p>
    <p>The academic excellence of our programmes, the international dimension of our training and our professional work placements at the most prestigious hotels in the world all ensure that our graduates are certain to secure a career in a strategic role in the luxury sector. Half of our students sign a permanent contract before they even finish their final work placement.</p>
  </div>

  <div class="photo" role="img" aria-label="Photograph of the four members of the school’s management team in a grand hotel salon with chandeliers, two seated on a green velvet sofa and two standing"></div>

  <p class="caption caption-fr" lang="fr"><b>De gauche à droite,</b> l’équipe de Direction de la Prestige Aubergerie dans les salons du Grand Hôtel Solenne : Laurent Vaudrey, Vice-Président, Nadia Ferrand, Directeur des opérations, Claire Montel, Responsable pédagogique, et Olivier Dessain, Président</p>
  <p class="caption caption-en" lang="en"><b>From left to right,</b> the PA Management team at the Grand Hôtel Solenne: Laurent Vaudrey, Vice-President, Nadia Ferrand, Operations Manager, Claire Montel, Education Manager and Olivier Dessain, President</p>

  <span class="folio folio-left">2</span>
  <span class="folio folio-right">3</span>
</main>
</body>
</html>
```